Stationary for security company
BRAMLOCK GUARDING LTD
Project: Stationary for security company
Stationary for security company  - Security
Creative Brief
Professional
148 MORTWELL CRESCENT DUNSBY KENT TN8 4QP
info@bramlock-guarding.co.uk
I DON'T NEED ADDRESS ON BUSINESS CARDS, JUST ON THE LETTER HEADS PLEASE.
specialize in:- -CCTV SYSTEMS -INTRUDER ALARMS -INTERCOM SYSTEMS -ELECTRICAL INSTALLATIONS UNDERTAKEN
delwynparfitt delwynparfitt
#183 I was referring to the back design back option 3 but in blue and with out the text just logo in centre. Also could you do me a design for invoices too?
#183 Hello, thank you for your designs I like the idea you have in design #183. Could you remove the phone number from the logo itself and complete the bottom line. We don't really need a number on the logo as we will have it on the stationary itself! And also the back of the business card you have in the design in black could you do that in blue, I like the blue and remove the text writing from the back of the card, so we just have the logo on the back. One more thing could you add Facebook and Twitter to the front of the business card please. Kind regards Delwyn Parfitt

```html
<!DOCTYPE html>
<html lang="en">
<head>
<meta charset="utf-8">
<title>Bramlock Guarding Ltd – Business Card</title>
<link rel="stylesheet" href="https://fonts.googleapis.com/css2?family=Exo+2:wght@400;600;700&display=swap">
<style>
  :root {
    --backdrop: #b9bbbe;
    --card: #ffffff;
    --brand-blue: #1d4fb8;
    --brand-blue-dark: #123a8c;
    --bar-dark: #2a2c30;
    --bar-dark-light: #4a4d52;
    --ink: #3d4045;
    --ink-soft: #7a7d82;
    --font: "Exo 2", Arial, sans-serif;
  }
  * { box-sizing: border-box; margin: 0; padding: 0; }
  html, body { width: 1200px; height: 895px; overflow: hidden; }
  body { background: var(--backdrop); font-family: var(--font); position: relative; }

  .card {
    position: absolute;
    width: 700px; height: 400px;
    left: 250px;
    background: var(--card);
    box-shadow: 0 6px 18px rgba(0,0,0,.18);
    overflow: hidden;
  }
  .card--back { top: 30px; }
  .card--front { top: 465px; }

  .brand { display: flex; align-items: center; gap: 10px; position: absolute; white-space: nowrap; }
  .brand__mark { width: 22px; height: 22px; background: var(--brand-blue); flex: none; }
  .brand__name { color: var(--brand-blue); font-weight: 700; letter-spacing: .5px; white-space: nowrap; }

  .card--back .brand { left: 50%; top: 50%; transform: translate(-50%, -50%); }
  .card--back .brand__name { font-size: 26px; }
  .card--back .brand__mark { width: 30px; height: 30px; }

  .card--front .brand { left: 30px; top: 48px; }
  .card--front .brand__name { font-size: 17px; }

  .band { position: absolute; left: 0; top: 150px; width: 700px; height: 50px; }
  .band__dark {
    position: absolute; left: 0; top: 0; width: 190px; height: 50px;
    background: linear-gradient(90deg, var(--bar-dark), var(--bar-dark-light));
  }
  .band__blue {
    position: absolute; left: 190px; top: 0; right: 0; height: 50px;
    background: linear-gradient(90deg, var(--brand-blue-dark), var(--brand-blue) 35%);
  }
  .band__web {
    position: absolute; left: 250px; top: 14px;
    color: #fff; font-size: 17px; letter-spacing: .6px; white-space: nowrap;
  }

  .person { position: absolute; right: 45px; top: 92px; text-align: left; }
  .person__name { color: var(--brand-blue); font-size: 21px; font-weight: 600; letter-spacing: 1px; white-space: nowrap; }
  .person__role { color: var(--ink); font-size: 13px; letter-spacing: 1px; }

  .contact-list { position: absolute; list-style: none; }
  .contact-list li {
    display: flex; align-items: center; gap: 10px;
    color: var(--ink); font-size: 12px; height: 24px; white-space: nowrap;
  }
  .contact-list svg { width: 14px; height: 14px; flex: none; }
  .contact-list--left { left: 30px; top: 214px; }
  .contact-list--right { left: 475px; top: 300px; }

  .icon-box { width: 14px; height: 14px; background: var(--brand-blue); flex: none; }
</style>
</head>
<body>

<section class="card card--back" aria-label="Business card back">
  <div class="brand">
    <span class="brand__mark"></span>
    <span class="brand__name">BRAMLOCK GUARDING LTD</span>
  </div>
</section>

<section class="card card--front" aria-label="Business card front">
  <div class="brand">
    <span class="brand__mark"></span>
    <span class="brand__name">BRAMLOCK GUARDING LTD</span>
  </div>

  <div class="person">
    <p class="person__name">OWEN HARTLEY</p>
    <p class="person__role">MANAGER</p>
  </div>

  <div class="band">
    <div class="band__dark"></div>
    <div class="band__blue"></div>
    <span class="band__web">www.bramlockguard.co.uk/123</span>
  </div>

  <ul class="contact-list contact-list--left">
    <li>
      <svg viewBox="0 0 14 14"><rect width="14" height="14" fill="var(--brand-blue)"/><path d="M4.5 3h1.6l.7 2-1 .7a5 5 0 0 0 2.5 2.5l.7-1 2 .7v1.6c0 .3-.3.5-.6.5A7 7 0 0 1 4 3.6c0-.3.2-.6.5-.6z" fill="#fff"/></svg>
      014 275 3918
    </li>
    <li>
      <svg viewBox="0 0 14 14"><rect width="14" height="14" fill="var(--brand-blue)"/><rect x="3" y="4.5" width="8" height="5.5" fill="none" stroke="#fff" stroke-width="1"/><path d="M3 4.5l4 3 4-3" fill="none" stroke="#fff" stroke-width="1"/></svg>
      office@bramlockmail.com
    </li>
  </ul>

  <ul class="contact-list contact-list--right">
    <li><span class="icon-box"></span>www.bramlockguard.co.uk</li>
    <li><span class="icon-box"></span>www.chirpline.com</li>
    <li><span class="icon-box"></span>www.friendwall.com</li>
  </ul>
</section>

</body>
</html>
```